IT Company Business Card design

Brisk Node is a new computer solutions business focusing on setting up servers and computer systems for small to medium sized businesses.

A business client will either request a solution, or support for a current system and we will turn up on site to provide these services.

We are bast in Christchurch, New Zealand.

We are looking for unique business card's that stand out and show off the business in a professional light.

Open to all idea's etc.

Industry/Entity Type

Computer

Requirements
Must have
• Business Logo (AI file attached)
Employee Name
Business title
Business landline number
Cell phone number
Email
Web URL
Nice to have
• Could be nice to have some keywords (possibly on the back) such as:

Business IT solutions
Network installations
Phone solutions
Server management
Software diagnostics

The above is not needed, just an idea.

```html
<!DOCTYPE html>
<html lang="en">
<head>
<meta charset="utf-8">
<title>Brisk Node – Business Card</title>
<link rel="stylesheet" href="https://fonts.googleapis.com/css2?family=Questrial&family=Open+Sans:wght@400&display=swap">
<style>
  :root {
    --paper: #ffffff;
    --frame: #9a9a9a;
    --ink-strong: #111111;
    --ink-soft: #404040;
    --cyan: #22e6f2;
    --cyan-bright: #1ff8fa;
    --blue-deep: #0a36a6;
    --blue-mid: #0d86cc;
    --mark-blue: #1560c8;
  }
  * { box-sizing: border-box; margin: 0; padding: 0; }
  html, body {
    width: 1200px;
    height: 776px;
    overflow: hidden;
    background: var(--paper);
  }
  .card {
    position: absolute;
    left: 35px;
    top: 68px;
    width: 1130px;
    height: 654px;
    border: 3px solid var(--frame);
    background: var(--paper);
  }
  .accent-top {
    position: absolute;
    left: 0;
    top: 0;
    width: 266px;
    height: 44px;
    background: linear-gradient(90deg, var(--cyan) 0%, #18a8de 45%, var(--blue-deep) 100%);
  }
  .accent-bottom {
    position: absolute;
    right: 0;
    bottom: 8px;
    width: 547px;
    height: 38px;
    background: linear-gradient(90deg, var(--cyan-bright) 0%, var(--cyan-bright) 65%, #22e2f4 75%, var(--blue-mid) 100%);
  }
  .brand {
    position: absolute;
    left: 132px;
    top: 117px;
    display: flex;
    align-items: center;
    gap: 34px;
  }
  .brand-dot {
    width: 120px;
    height: 120px;
    border-radius: 50%;
    background: var(--mark-blue);
  }
  .brand-name {
    font-family: "Questrial", "Century Gothic", sans-serif;
    font-size: 40px;
    letter-spacing: 5px;
    color: var(--ink-strong);
    text-transform: uppercase;
    line-height: 1;
  }
  .contact {
    position: absolute;
    left: 581px;
    top: 265px;
    font-family: "Open Sans", "Myriad Pro", sans-serif;
    color: var(--ink-soft);
  }
  .person-name {
    font-size: 30px;
    color: var(--ink-strong);
    line-height: 40px;
  }
  .person-title {
    font-size: 30px;
    line-height: 40px;
    margin-bottom: 42px;
  }
  .details {
    list-style: none;
    font-size: 30px;
    line-height: 42px;
  }
  .details li {
    display: grid;
    grid-template-columns: 40px 38px auto;
  }
</style>
</head>
<body>
  <div class="card">
    <div class="accent-top"></div>

    <div class="brand">
      <div class="brand-dot"></div>
      <span class="brand-name">Brisk Node</span>
    </div>

    <div class="contact">
      <p class="person-name">Employee Name</p>
      <p class="person-title">Business title</p>
      <ul class="details">
        <li><span>L</span><span>:</span><span>022 XXXXXXX</span></li>
        <li><span>M</span><span>:</span><span>+91 XXXXXXXX</span></li>
        <li><span>E</span><span>:</span><span>employee@brisknode.com</span></li>
        <li><span>W</span><span>:</span><span>www.brisknode.com</span></li>
      </ul>
    </div>

    <div class="accent-bottom"></div>
  </div>
</body>
</html>
```